Analytics/BI tech start-up seeks sharp, creative, simple, secret agent type logo & theme

"Quill 9 Dynamics" seeks a logo design/color scheme template for NYC based tech start-up of software engineers, solutions architects, and data/BI analysts. We develop reporting solutions and analytics platforms for small-medium sized businesses. We code for database, cloud, and web/mobile apps.<br/><br/>Some *very basic, limited* sketches are attached to show ideas we've had. We need a logo and color scheme that may be used for business cards, paper letterhead and envelopes, and web pages to be published at "www.quill9.dev".<br/><br/>We like the black/red, red/white, blue/black, white/black contrasts as a stating point, and prefer black background business cards, but open to anything if it feels like a good match. We are relying on the projects submitted here to take care of the creativity part of our image, which we work on logistics to launching our start-up. Something that could also be easily translated into black/white, grayscale would be appreciated as well. while log is important, we also need an icon that may be used as an app thumbnail. For font, we prefer all caps.<br/><br/>Business: Quill 9 Dynamics<br/>Slogan: If. Else. Us. / If -> Else -> Us / If - Else - Us / etc.<br/>Website: www.quill.dev<br/>Icon: [Q9] , only as a starting point<br/>Theme Ideas: Sleek, futuristic, secret agent-like tech, simple, bold color contrasts, software code related<br/><br/>Feel free to reach out to jdrevnik@mailvora.net as a contact for any questions or follow up. We look forward to seeing amazing ideas!
Updates

We would like to provide the opportunity for as many different submissions as possible.

Target Market(s)

Small business owners, entrepreneurs, financial/tech companies, freelance engineers, people in need of IT assistance to elevate business

Industry/Entity Type

It Company

Contact Information for Business Card

Individual Info: Name, Position, Phone Number 1, Phone Number 2 (optional), Fax Number, email Address.
Company Info: Name, logo, icon (optional), web site, slogan

Font styles to use
Sans Serif
Other font styles liked:
• Similar to Biome Light All Caps, Hollow Meridian type style

Requirements
Must have
• Pronounced 1 in the logo, either in the word Quill or not. Bold color contrast, one side with only logo or icon, possible web address too. Other side with all individual info plus logo, and/or icon and web address. If using uploaded files as a base, center the C more between the E and T, it is too closer to the T as is.
Nice to have
• Bolder font possibly, more square edged at ends of letters but still with minor curved corners. Icon suggested as a starting point is “[Q9]” and instead of a slogan, use "Data - Cloud - Web - Software" and the dividers don't necessary have to be hyphens.
Should not have
• Open to all creative ideas, try anything. Please come up with different logos than are in the attached files, they are meant as a starting point.

```html
<!DOCTYPE html>
<html lang="en">
<head>
<meta charset="utf-8">
<title>Quill 9 Dynamics — Business Card</title>
<link rel="stylesheet" href="https://fonts.googleapis.com/css2?family=Arimo:wght@400;700&display=swap">
<style>
  :root {
    --navy: #0b1f45;
    --green: #25960c;
    --white: #ffffff;
    --ink: #1d1d1f;
    --rule: #c9ccd3;
    --backdrop: #e6e7ea;
  }
  * { box-sizing: border-box; margin: 0; padding: 0; }
  html, body { width: 1200px; height: 1015px; overflow: hidden; }
  body {
    background: var(--backdrop);
    font-family: "Arimo", Arial, sans-serif;
    display: flex;
    flex-direction: column;
    align-items: center;
    justify-content: center;
    gap: 44px;
  }
  .card {
    width: 760px;
    height: 434px;
    position: relative;
    overflow: hidden;
    box-shadow: 0 6px 18px rgba(0,0,0,.18);
  }

  /* Front */
  .card--front { background: var(--navy); }
  .front__band {
    position: absolute; left: 0; right: 0; bottom: 0; height: 150px;
    background: var(--green);
  }
  .front__wordmark {
    position: absolute; left: 0; right: 0; top: 172px;
    text-align: center;
    color: var(--white);
    font-weight: 700;
    font-size: 56px;
    line-height: 1;
    letter-spacing: 4px;
    text-transform: uppercase;
  }
  .front__tagline {
    position: absolute; left: 0; right: 0; bottom: 80px;
    text-align: center;
    color: var(--white);
    font-size: 19px;
    letter-spacing: .5px;
  }
  .front__tagline .dot {
    display: inline-block; width: 7px; height: 7px;
    background: var(--white); margin: 0 14px; vertical-align: middle;
  }

  /* Back */
  .card--back { background: var(--white); }
  .back__footer {
    position: absolute; left: 0; right: 0; bottom: 0; height: 118px;
    background: var(--navy);
    color: var(--white);
    font-size: 22px;
    letter-spacing: 2px;
    display: flex; align-items: center; justify-content: center;
    padding-left: 180px;
  }
  .back__brand {
    position: absolute; left: 40px; top: 70px; width: 330px;
    display: flex; flex-direction: column; align-items: flex-start; gap: 22px;
  }
  .brand__square {
    width: 110px; height: 110px; background: var(--green);
  }
  .brand__name {
    color: var(--navy);
    font-weight: 700;
    font-size: 34px;
    letter-spacing: 2px;
    text-transform: uppercase;
    line-height: 1.1;
  }
  .back__divider {
    position: absolute; left: 392px; top: 52px; width: 1px; height: 228px;
    background: var(--rule);
  }
  .back__contact {
    position: absolute; left: 420px; top: 52px; width: 310px;
    color: var(--ink);
  }
  .contact__name {
    font-weight: 700; font-size: 24px; color: var(--navy); letter-spacing: .5px;
  }
  .contact__name .surname { color: var(--green); }
  .contact__title { font-size: 17px; margin-top: 2px; }
  .contact__list { list-style: none; margin-top: 24px; font-size: 17px; line-height: 1.35; }
  .contact__list li { display: flex; align-items: center; gap: 8px; }
  .contact__list svg { width: 14px; height: 14px; fill: var(--green); flex: none; }
  .contact__address { margin-top: 18px; font-size: 17px; line-height: 1.35; }
</style>
</head>
<body>

  <section class="card card--front" aria-label="Card front">
    <div class="front__band"></div>
    <div class="front__wordmark">Quill 9 Dynamics</div>
    <div class="front__tagline">
      Data<span class="dot"></span>Cloud<span class="dot"></span>Web<span class="dot"></span>Development
    </div>
  </section>

  <section class="card card--back" aria-label="Card back">
    <div class="back__brand">
      <div class="brand__square"></div>
      <div class="brand__name">Quill 9<br>Dynamics</div>
    </div>

    <div class="back__divider"></div>

    <div class="back__contact">
      <div class="contact__name">LORUM <span class="surname">SMITH</span></div>
      <div class="contact__title">Managing Director</div>
      <ul class="contact__list">
        <li>
          <svg viewBox="0 0 16 16" aria-hidden="true"><path d="M3 1h3l1.5 4-2 1.2a9 9 0 0 0 4.3 4.3L11 8.5l4 1.5v3c0 1-1 2-2 2C6.4 15 1 9.6 1 3c0-1 1-2 2-2z"/></svg>
          212 730 4190
        </li>
        <li>
          <svg viewBox="0 0 16 16" aria-hidden="true"><path d="M4 1h8v4H4zM1 6h14v6h-3v3H4v-3H1zm4 4v4h6v-4z"/></svg>
          212 730 4191
        </li>
        <li>
          <svg viewBox="0 0 16 16" aria-hidden="true"><path d="M1 3h14v10H1zm1.5 1.5L8 9l5.5-4.5z"/></svg>
          info@quillnine.net
        </li>
      </ul>
      <div class="contact__address">Address line goes here<br>Second line here pincode</div>
    </div>

    <div class="back__footer">www.quill.dev</div>
  </section>

</body>
</html>
```